A Label for an ECO Friendly Spirit Company

Design a label which can be used for vodka and gin (London Dry Gin). It should be Square type Like the Shape File you see in the uploads. VORN means Local Eco friendly Authentic and Fair. We want a cool and slim label that calls for eco-friendly. We want to use it for our premium
Vodka and our London Dry Gin. Please use the logo and design it in Square Type.

40%vol, 700ml

Target Market(s)

spirits and events

Industry/Entity Type

SPIRITS

Colors
00AB8E
00BBA5
67D7C9
C6EFE9
E9F9F6
59FF00
82FF00
B8FF75
E3FFCB
F4FFEA

Requirements
Must have
• Logo from VORN, Squaee Shape

```html
<!DOCTYPE html>
<html lang="en">
<head>
<meta charset="utf-8">
<title>VORN London Dry Gin Label</title>
<link href="https://fonts.googleapis.com/css2?family=Libre+Baskerville:wght@700&family=Montserrat:wght@600&family=Open+Sans:wght@400&family=Great+Vibes&display=swap" rel="stylesheet">
<style>
  :root {
    --page: #f5f6f8;
    --label-fill: #eceff1;
    --label-frame: #ffffff;
    --brand: #00AB8E;
    --wash-green: #dcedc8;
    --wash-mint: #c6efe9;
    --ink: #3d3d3d;
    --ink-soft: #4a4a4a;
    --paper: #ffffff;
    --tape: #e4e4e4;
  }
  * { margin: 0; padding: 0; box-sizing: border-box; }
  html, body { width: 1200px; height: 1086px; overflow: hidden; background: var(--page); }
  .label { position: relative; width: 1200px; height: 1086px; }
  .label-shape { position: absolute; inset: 0; }
  .brand {
    position: absolute; left: 0; width: 1200px; top: 332px; height: 80px;
    display: flex; justify-content: center; align-items: center; gap: 18px;
  }
  .brand-square { width: 74px; height: 74px; background: var(--brand); border-radius: 6px; }
  .brand-name {
    font-family: "Montserrat", sans-serif; font-weight: 600;
    font-size: 74px; line-height: 1; color: var(--brand); letter-spacing: 2px;
  }
  .tag {
    position: absolute; left: 352px; top: 494px; width: 497px; height: 260px;
    background: var(--paper);
    clip-path: polygon(0 0,100% 0,100% 93%,96% 95%,92% 92%,88% 96%,83% 93%,78% 97%,72% 94%,66% 96%,60% 93%,54% 97%,48% 94%,42% 96%,36% 93%,30% 97%,24% 94%,18% 96%,12% 93%,6% 97%,0 95%);
  }
  .tag p, .tag h1 { position: absolute; left: 0; width: 100%; text-align: center; line-height: 1; }
  .product-name {
    top: 76px;
    font-family: "Libre Baskerville", serif; font-weight: 700;
    font-size: 36px; letter-spacing: 2.5px; color: var(--ink);
  }
  .origin {
    top: 143px;
    font-family: "Open Sans", sans-serif; font-size: 17px;
    letter-spacing: 1.2px; color: var(--ink-soft);
  }
  .blend {
    top: 184px;
    font-family: "Great Vibes", cursive; font-size: 30px; color: var(--ink);
  }
  .tape {
    position: absolute; left: 512px; top: 470px; width: 126px; height: 58px;
    background: var(--tape); opacity: 0.9; transform: rotate(-2deg);
  }
  .volume {
    position: absolute; left: 0; width: 1200px; top: 953px; text-align: center; line-height: 1;
    font-family: "Open Sans", sans-serif; font-size: 20px; letter-spacing: 2px; color: var(--ink-soft);
  }
</style>
</head>
<body>
<main class="label">
  <svg class="label-shape" width="1200" height="1086" viewBox="0 0 1200 1086">
    <defs>
      <clipPath id="diamond-clip">
        <polygon points="600,63 1080,543 600,1023 120,543"/>
      </clipPath>
      <linearGradient id="art-wash" x1="0" y1="0" x2="0" y2="1">
        <stop offset="0" stop-color="var(--wash-green)"/>
        <stop offset="0.5" stop-color="var(--label-fill)"/>
        <stop offset="1" stop-color="var(--wash-mint)"/>
      </linearGradient>
    </defs>
    <rect class="label-art" role="img" aria-label="Painted green and mint botanical brushstroke artwork"
      x="120" y="63" width="960" height="960" fill="url(#art-wash)" clip-path="url(#diamond-clip)"/>
    <polygon class="label-frame" points="600,63 1080,543 600,1023 120,543" fill="none" stroke="var(--label-frame)" stroke-width="12"/>
  </svg>

  <div class="brand">
    <span class="brand-square"></span>
    <span class="brand-name">VORN</span>
  </div>

  <section class="tag">
    <h1 class="product-name">LONDON DRY GIN</h1>
    <p class="origin">PRODUCED &amp; BOTTLED IN GERMANY</p>
    <p class="blend">Signature Blend</p>
  </section>
  <div class="tape"></div>

  <p class="volume">40%vol | 700ml</p>
</main>
</body>
</html>
```